Hip / Cool Business Card for Custom Accessory Company

I would like to get a 2 sided design for standard size business cards, glossy (2 inches x 3.5 inches). Can be landscape or portrait layout! The design should include our logo (attached). The card should be extremely clear that the company is Tin Lantern. Should also have our URL clear. Should also use the color scheme seen on our upcoming site, tinlantern-example.com. The font we use is called "hurry up." Other than that, please go-to-town. We are targeting 15-45 y.o. market, with a skew on the 20-30 crowd. We do custom and stock iPhone cases as well as Cufflinks, Winestoppers; see the website for more.
Updates

Project Deadline Extended
Reason: Extending in case the US July 4th Holiday is keeping people from working!!

Industry/Entity Type

Landscape

Requirements
Must have
• Must be clear that the website is tinlantern-example.com. Must be clear that custom designs are an option.
Nice to have
• images of our designs. examples of our designs.
Should not have
• hard on the eyes contrasting colors such as orange on black. green on blue. Should not have any fonts that are considered "old" like Times New Roman. But decorative fonts are fine.

```html
<!DOCTYPE html>
<html lang="en">
<head>
<meta charset="utf-8">
<title>Tin Lantern Business Card</title>
<link href="https://fonts.googleapis.com/css2?family=Lato:wght@400;700;900&display=swap" rel="stylesheet">
<style>
  :root {
    --bg: #ecebe8;
    --card: #ffffff;
    --teal: #2fb3bd;
    --teal-deep: #1f9aa5;
    --ink: #2b2b2b;
    --muted: #4a4a4a;
    --white: #ffffff;
  }
  html, body {
    margin: 0;
    width: 1200px;
    height: 913px;
    overflow: hidden;
    background: var(--bg);
    font-family: "Lato", Arial, sans-serif;
  }
  .canvas {
    position: relative;
    width: 1200px;
    height: 913px;
  }
  .card {
    position: absolute;
    width: 520px;
    height: 297px;
    background: var(--card);
    border-radius: 18px;
    overflow: hidden;
    box-shadow: 0 6px 18px rgba(0,0,0,0.18);
  }
  .card-front { left: 50px; top: 308px; }
  .card-back  { left: 630px; top: 308px; }

  .brand {
    display: flex;
    align-items: center;
    gap: 12px;
    color: var(--ink);
    font-weight: 900;
    letter-spacing: 1px;
    text-transform: uppercase;
    white-space: nowrap;
  }
  .brand-dot {
    border-radius: 50%;
    background: var(--teal);
    flex: none;
  }
  .front-brand {
    position: absolute;
    left: 0; right: 0; top: 100px;
    justify-content: center;
    font-size: 36px;
  }
  .front-brand .brand-dot { width: 46px; height: 46px; }
  .front-url {
    position: absolute;
    left: 0; right: 0; top: 166px;
    text-align: center;
    color: var(--teal);
    font-weight: 900;
    font-size: 19px;
  }
  .front-tagline {
    position: absolute;
    left: 0; right: 0; top: 196px;
    text-align: center;
    color: var(--muted);
    font-size: 12px;
    letter-spacing: 2px;
    text-transform: uppercase;
  }

  .back-wave { position: absolute; inset: 0; }
  .back-name {
    position: absolute;
    left: 290px; top: 34px;
    color: var(--teal);
    font-weight: 700;
    font-size: 17px;
    white-space: nowrap;
  }
  .back-title {
    position: absolute;
    left: 290px; top: 56px;
    color: var(--muted);
    font-size: 11px;
    white-space: nowrap;
  }
  .back-address {
    position: absolute;
    left: 362px; top: 106px;
    color: var(--white);
    font-size: 11px;
    line-height: 14px;
    white-space: nowrap;
  }
  .back-contacts {
    position: absolute;
    left: 338px; top: 172px;
    margin: 0; padding: 0;
    list-style: none;
    color: var(--white);
    font-size: 10.5px;
    line-height: 16px;
    white-space: nowrap;
  }
  .back-contacts li { display: flex; align-items: center; gap: 6px; }
  .contact-icon {
    width: 9px; height: 9px;
    border-radius: 50%;
    border: 1.5px solid var(--white);
    box-sizing: border-box;
    flex: none;
  }
  .back-brand {
    position: absolute;
    left: 26px; top: 190px;
    font-size: 22px;
  }
  .back-brand .brand-dot { width: 30px; height: 30px; }
</style>
</head>
<body>
<main class="canvas">
  <section class="card card-front" aria-label="Card front">
    <div class="brand front-brand"><span class="brand-dot"></span>Tin Lantern</div>
    <div class="front-url">tinlantern-example.com</div>
    <div class="front-tagline">Custom &amp; stock designs</div>
  </section>

  <section class="card card-back" aria-label="Card back">
    <svg class="back-wave" width="520" height="297" viewBox="0 0 520 297">
      <defs>
        <linearGradient id="tealFill" x1="0" y1="0" x2="1" y2="1">
          <stop offset="0" stop-color="#3cc3cb"/>
          <stop offset="1" stop-color="#1f9aa5"/>
        </linearGradient>
      </defs>
      <path d="M500 0 C390 8 355 120 295 195 C250 255 195 290 130 297 L520 297 L520 0 Z" fill="url(#tealFill)"/>
      <path d="M495 0 C385 8 350 118 290 193 C245 253 190 288 125 297" fill="none" stroke="#2b2b2b" stroke-width="4"/>
    </svg>
    <div class="back-name">Rowan Ellery</div>
    <div class="back-title">Founder &amp; CEO</div>
    <div class="back-address">Tin Lantern<br>418 Quarry Lane Suite 12<br>Fairview, VA 20100</div>
    <ul class="back-contacts">
      <li><span class="contact-icon"></span>555.010.0000</li>
      <li><span class="contact-icon"></span>555.010.7890</li>
      <li><span class="contact-icon"></span>support@tinlantern-example.com</li>
      <li><span class="contact-icon"></span>tinlantern-example.com</li>
    </ul>
    <div class="brand back-brand"><span class="brand-dot"></span>Tin Lantern</div>
  </section>
</main>
</body>
</html>
```